Prestige Car Bodyshop Business Card

We are a car bodyshop based in the UK. Our customer base is mainly prestige high-value vehicles. I am looking for a classy and stylish business card design for my staff to give out to customers, with their direct email and phone number, as well as our main email and phone number with address details

I am also looking to have a general business card design with just our main company address and contact details, but also have a space to add a manufacturer approval logo (i.e Falcora, Vexa, Torvik etc... logo) in the corner somewhere.

I do not particularly want any outlines or pictures of cars on the card, I would just like a quality high-end look.

Please feel free to get in touch if you have any questions or queries?

Many Thanks

Gordon

Target Market(s)

Prestige vehicle owners

Industry/Entity Type

Automotive

Contact Information for Business Card

I am looking for a classy and stylish business card design for my staff to give out to customers, with their direct email and phone number, as well as our main email and phone number with address details

Font styles to use
Sans Serif

Colors

Designer to choose colors to be used in the design.

Requirements
Nice to have
• I do not particularly want any outlines or pictures of cars on the card, I would just like a quality high-end look.

```html
<!DOCTYPE html>
<html lang="en">
<head>
<meta charset="utf-8">
<title>Halden Bodyworks – Business Card</title>
<link rel="stylesheet" href="https://fonts.googleapis.com/css2?family=Roboto:wght@300;400;700&display=swap">
<style>
  :root {
    --paper: #ffffff;
    --brand-blue: #0443d8;
    --brand-blue-dark: #0a2fa0;
    --logo-blue: #0a2a8c;
    --panel-black: #000000;
    --ink-light: #ffffff;
  }
  * { margin: 0; padding: 0; box-sizing: border-box; }
  html, body {
    width: 1200px; height: 720px; overflow: hidden;
    background: var(--paper);
    font-family: "Roboto", Arial, sans-serif;
  }
  .card {
    position: relative; width: 1200px; height: 720px;
    background: var(--paper); overflow: hidden;
  }
  .card-shapes { position: absolute; inset: 0; }
  .brand {
    position: absolute; left: 100px; top: 101px;
    display: flex; align-items: center; gap: 20px;
  }
  .brand-dot {
    width: 88px; height: 88px; border-radius: 50%;
    background: var(--brand-blue);
  }
  .brand-name {
    color: var(--logo-blue); font-weight: 400;
    font-size: 30px; letter-spacing: 1px; text-transform: uppercase;
  }
  .holder {
    position: absolute; left: 85px; top: 315px;
    display: flex; align-items: flex-start; gap: 36px;
    color: var(--ink-light);
  }
  .holder-icon { width: 34px; height: 34px; margin-top: 24px; }
  .holder-name {
    font-weight: 700; font-size: 47px; line-height: 1.05;
    text-transform: uppercase;
  }
  .holder-role { font-weight: 400; font-size: 25px; line-height: 1.2; }
  .contacts {
    position: absolute; left: 690px; top: 226px;
    list-style: none; color: var(--ink-light);
    font-weight: 300; font-size: 30px; line-height: 38px;
  }
  .contact { display: flex; align-items: flex-start; gap: 35px; margin-bottom: 22px; }
  .contact-icon { width: 34px; height: 34px; flex: none; margin-top: 2px; }
</style>
</head>
<body>
<main class="card">
  <svg class="card-shapes" width="1200" height="720" viewBox="0 0 1200 720" aria-hidden="true">
    <polygon class="contact-panel" points="656,160 1200,160 1200,557 571,557" fill="var(--panel-black)"/>
    <polygon class="name-band" points="0,273 656,273 617,446 0,446" fill="var(--brand-blue)"/>
    <polygon class="name-band-fold" points="592,446 617,446 592,461" fill="var(--brand-blue-dark)"/>
  </svg>

  <div class="brand">
    <span class="brand-dot"></span>
    <span class="brand-name">Halden Bodyworks</span>
  </div>

  <div class="holder">
    <svg class="holder-icon" viewBox="0 0 24 24" aria-hidden="true">
      <circle cx="12" cy="7.5" r="5" fill="currentColor"/>
      <path d="M2 23c0-5 4-8.5 10-8.5s10 3.5 10 8.5z" fill="currentColor"/>
    </svg>
    <div>
      <h1 class="holder-name">Rowan Ellery</h1>
      <p class="holder-role">CEO</p>
    </div>
  </div>

  <ul class="contacts">
    <li class="contact">
      <svg class="contact-icon" viewBox="0 0 24 24" aria-hidden="true"><path fill="currentColor" d="M6.6 10.8a15.1 15.1 0 0 0 6.6 6.6l2.2-2.2a1 1 0 0 1 1-.25 11.4 11.4 0 0 0 3.6.57 1 1 0 0 1 1 1V20a1 1 0 0 1-1 1A17 17 0 0 1 3 4a1 1 0 0 1 1-1h3.5a1 1 0 0 1 1 1c0 1.25.2 2.45.57 3.57a1 1 0 0 1-.25 1z"/></svg>
      <span>555-014-2290</span>
    </li>
    <li class="contact">
      <svg class="contact-icon" viewBox="0 0 24 24" aria-hidden="true"><path fill="currentColor" d="M2 5h20v1.2l-10 6.3L2 6.2zM2 8.6l10 6.3 10-6.3V19H2z"/></svg>
      <span>info@haldenbody.com</span>
    </li>
    <li class="contact">
      <svg class="contact-icon" viewBox="0 0 24 24" aria-hidden="true" fill="none" stroke="currentColor" stroke-width="1.8"><circle cx="12" cy="12" r="10"/><ellipse cx="12" cy="12" rx="4.5" ry="10"/><path d="M2 12h20M3.5 7h17M3.5 17h17M12 2v20"/></svg>
      <span>www.haldenbody.com</span>
    </li>
    <li class="contact">
      <svg class="contact-icon" viewBox="0 0 24 24" aria-hidden="true"><path fill="currentColor" d="M12 1a7.5 7.5 0 0 0-7.5 7.5C4.5 14 12 23 12 23s7.5-9 7.5-14.5A7.5 7.5 0 0 0 12 1zm0 10.2a2.7 2.7 0 1 1 0-5.4 2.7 2.7 0 0 1 0 5.4z"/></svg>
      <span>2180 Linden Avenue<br>Marlow,TX 77019</span>
    </li>
  </ul>
</main>
</body>
</html>
```